Start up in business consultancy needs a business card

We need the business card's layout (we have already the logo). Our business is concerned on consultancy services delivered to companies on the matter of sustainability. Business card should be enough essentials and professional style.

Side A with the following info:
logo + a space for the claim (still to identify) + website of the company

Side B with the following info:
Name of business card holder + title of the business card holder + address of the company + space for mobile number, phone number, fax number + e-mail of business card holder + graphic details around.

Target Market(s)

Business of any sector

Industry/Entity Type

Business Service

Contact Information for Business Card

Name of the company:
Pianoverde srl
Società Benefit

Address of the company:
Via Lucerna, 7
21047 - Saronno (VA)

Website:
www.pianoverde.it

Name of the BC' holder:
Luca Ferentino

Title:
Co-fondatore

Email:
luca@pianoverde.it

Mobile:
+39 348 915 2074
Phone:
+39 348 915 2074
Fax:
+39 348 915 2074

Font styles to use
Other font styles liked:
• new gothic

```html
<!DOCTYPE html>
<html lang="it">
<head>
<meta charset="utf-8">
<title>Pianoverde – biglietto da visita</title>
<link rel="stylesheet" href="https://fonts.googleapis.com/css2?family=Montserrat:wght@400;500;600&display=swap">
<style>
  :root {
    --brand-red: #d4442a;
    --paper: #f3f2f0;
    --ink: #111111;
    --faint: #dddcda;
    --canvas: #e7e4df;
  }
  * { box-sizing: border-box; margin: 0; padding: 0; }
  html, body {
    width: 1200px; height: 1000px; overflow: hidden;
    background: var(--canvas);
    font-family: "Montserrat", Arial, sans-serif;
  }
  .card {
    position: absolute;
    background: var(--paper);
    overflow: hidden;
    box-shadow: 0 4px 10px rgba(0,0,0,0.18);
  }
  .card--front { left: 232px; top: 54px; width: 723px; height: 413px; }
  .card--back  { left: 235px; top: 532px; width: 720px; height: 410px; }
  .card__shapes { position: absolute; inset: 0; }

  .brand {
    position: absolute;
    display: flex; align-items: center; gap: 18px;
    color: var(--ink); font-weight: 500;
  }
  .brand__circle {
    border: 5px solid var(--ink); border-radius: 50%;
    flex: none;
  }
  .card--front .brand { left: 168px; top: 156px; font-size: 36px; letter-spacing: 0.2px; }
  .card--front .brand__circle { width: 112px; height: 112px; }

  .holder { position: absolute; left: 98px; top: 57px; }
  .holder__name { font-size: 24px; font-weight: 600; color: var(--ink); line-height: 1.1; }
  .holder__title { font-size: 19px; font-weight: 500; color: var(--brand-red); line-height: 1.2; }

  .contacts { position: absolute; left: 98px; top: 170px; list-style: none; }
  .contact {
    display: flex; align-items: center; gap: 9px;
    color: #fff; font-size: 15.5px; line-height: 1.35;
    margin-bottom: 12px;
  }
  .contact__icon {
    width: 40px; height: 40px; border-radius: 50%;
    background: var(--ink); flex: none;
    display: flex; align-items: center; justify-content: center;
  }
  .contact--address { align-items: flex-start; }
  .phones {
    position: absolute; left: 101px; top: 329px;
    font-size: 14.5px; font-weight: 500; color: var(--ink);
  }
  .phones__number { color: #fff; font-weight: 400; }

  .card--back .brand {
    position: absolute; left: 512px; top: 206px;
    width: 184px; height: 184px; justify-content: center;
    border: 5px solid var(--ink); border-radius: 50%;
    font-size: 24px;
  }
</style>
</head>
<body>

<section class="card card--front" aria-label="Fronte">
  <svg class="card__shapes" width="723" height="413" viewBox="0 0 723 413" aria-hidden="true">
    <rect width="723" height="413" fill="var(--paper)"/>
    <circle cx="604" cy="112" r="66" fill="none" stroke="var(--faint)" stroke-width="4"/>
    <polygon points="0,0 723,261 723,413 0,413" fill="var(--brand-red)"/>
  </svg>
  <div class="brand">
    <span class="brand__circle" aria-hidden="true"></span>
    <span class="brand__name">pianoverde</span>
  </div>
</section>

<section class="card card--back" aria-label="Retro">
  <svg class="card__shapes" width="720" height="410" viewBox="0 0 720 410" aria-hidden="true">
    <rect width="720" height="410" fill="var(--paper)"/>
    <circle cx="305" cy="115" r="76" fill="none" stroke="var(--faint)" stroke-width="4"/>
    <rect y="158" width="720" height="252" fill="var(--brand-red)"/>
  </svg>

  <div class="holder">
    <p class="holder__name">Luca Ferentino</p>
    <p class="holder__title">Co-fondatore</p>
  </div>

  <ul class="contacts">
    <li class="contact contact--address">
      <span class="contact__icon">
        <svg width="18" height="22" viewBox="0 0 18 22" aria-hidden="true">
          <path d="M9 1a7 7 0 0 0-7 7c0 5 7 13 7 13s7-8 7-13a7 7 0 0 0-7-7z" fill="#fff"/>
          <circle cx="9" cy="8" r="2.6" fill="var(--ink)"/>
        </svg>
      </span>
      <span>Via Lucerna, 7<br>21047 - Saronno (VA)</span>
    </li>
    <li class="contact">
      <span class="contact__icon">
        <svg width="22" height="16" viewBox="0 0 22 16" aria-hidden="true">
          <rect x="1" y="1" width="20" height="14" fill="none" stroke="#fff" stroke-width="1.6"/>
          <path d="M1 1l10 8 10-8" fill="none" stroke="#fff" stroke-width="1.6"/>
        </svg>
      </span>
      <span>luca@pianoverde.it</span>
    </li>
    <li class="contact">
      <span class="contact__icon">
        <svg width="24" height="24" viewBox="0 0 24 24" aria-hidden="true" fill="none" stroke="#fff" stroke-width="1.4">
          <circle cx="12" cy="12" r="10"/>
          <ellipse cx="12" cy="12" rx="4.5" ry="10"/>
          <path d="M2 12h20M4 6.5h16M4 17.5h16M12 2v20"/>
        </svg>
      </span>
      <span>www.pianoverde.it</span>
    </li>
  </ul>

  <p class="phones">Mobile / Tel. / Fax: <span class="phones__number">+39 348 915 2074</span></p>

  <div class="brand"><span class="brand__name">pianoverde</span></div>
</section>

</body>
</html>
```